Party planning business card design

Galas with Wren is a party planning business

Function Planning: Weddings/Themed Parties/Children's Parties

Adult and Children's Photo Booths
Party Themed boxes,
We can find the venue, entertainment. face painters.

Children's costumes and accessories - Sell / Hire

Web: www.galaswithwren.example
Facebook: Galas with Wren

Industry/Entity Type

Party Planning

Contact Information for Business Card

Galas With Wren, Rosalind Pektrew,
Creative Director

Colors
e34297
000000

Requirements
Must have
• on my logo are you able to edit the stars to pink?

```html
<!DOCTYPE html>
<html lang="en">
<head>
<meta charset="utf-8">
<title>Galas with Wren – Business Card</title>
<link rel="stylesheet" href="https://fonts.googleapis.com/css2?family=Parisienne&family=Arimo:wght@400&display=swap">
<style>
  :root {
    --brand-pink: #e34297;
    --band-light: #f08ac4;
    --band-deep: #d9428f;
    --ornament-tone: #c23a80;
    --ink: #000000;
    --text-dark: #2a1a24;
    --text-muted: #4a4a4a;
    --card-white: #fbfbfb;
    --card-shade: #e9e9e9;
    --page-bg: #eceeef;
  }
  html, body {
    margin: 0;
    width: 1200px;
    height: 1023px;
    overflow: hidden;
    background: var(--page-bg);
  }
  .canvas {
    width: 1200px;
    height: 1023px;
    display: flex;
    align-items: center;
    justify-content: center;
  }
  .business-card {
    position: relative;
    width: 1000px;
    height: 560px;
    background: linear-gradient(180deg, var(--card-white) 0%, var(--card-shade) 100%);
    box-shadow: 0 18px 40px rgba(0,0,0,0.25);
    overflow: hidden;
  }
  .brand-area {
    position: absolute;
    left: 0; top: 0;
    width: 100%;
    height: 296px;
  }
  .logo-mark {
    position: absolute;
    left: 60px;
    top: 196px;
    display: flex;
    align-items: center;
    gap: 12px;
    font-family: "Arimo", sans-serif;
    font-size: 26px;
    line-height: 1;
    color: var(--brand-pink);
  }
  .logo-dot {
    width: 22px;
    height: 22px;
    border-radius: 50%;
    background: var(--brand-pink);
  }
  .brand-title {
    position: absolute;
    right: 60px;
    top: 108px;
    margin: 0;
    font-family: "Parisienne", cursive;
    font-weight: 400;
    font-size: 92px;
    line-height: 1;
    color: var(--ink);
  }
  .contact-person {
    position: absolute;
    right: 64px;
    top: 244px;
    margin: 0;
    font-family: "Arimo", sans-serif;
    font-size: 22px;
    line-height: 1;
    color: var(--text-muted);
  }
  .contact-band {
    position: absolute;
    left: 0; bottom: 0;
    width: 100%;
    height: 260px;
    background: linear-gradient(90deg, var(--band-deep) 0%, var(--band-light) 45%, var(--band-light) 60%, var(--band-deep) 100%);
    border-top: 4px solid var(--ink);
  }
  .contact-list {
    list-style: none;
    margin: 0;
    padding: 0;
    position: absolute;
    left: 0; right: 0;
    top: 40px;
    text-align: center;
    font-family: "Arimo", sans-serif;
    font-size: 34px;
    line-height: 46px;
    color: var(--text-dark);
  }
  .flourish {
    position: absolute;
    width: 120px;
    height: 44px;
    border-radius: 6px;
    background: var(--ornament-tone);
    opacity: 0.55;
  }
  .flourish--bottom-left { left: 24px; bottom: 18px; }
  .flourish--top-right { right: 24px; top: 18px; }
</style>
</head>
<body>
  <main class="canvas">
    <section class="business-card">
      <div class="brand-area">
        <div class="logo-mark">
          <span class="logo-dot"></span>
          <span class="logo-name">Galas with Wren</span>
        </div>
        <h1 class="brand-title">Galas with Wren</h1>
        <p class="contact-person">Rosalind Pektrew, Creative Director</p>
      </div>
      <div class="contact-band">
        <div class="flourish flourish--top-right" role="img" aria-label="Black scroll ornament in the band corner"></div>
        <div class="flourish flourish--bottom-left" role="img" aria-label="Black scroll ornament in the band corner"></div>
        <ul class="contact-list">
          <li>Phone: 0400 123 987</li>
          <li>Web: www.galaswithwren.example</li>
          <li>Facebook: Galas with Wren</li>
          <li>Email: rosalind@galaswithwren.example</li>
        </ul>
      </div>
    </section>
  </main>
</body>
</html>
```